Redesign our iOS App Design mockups

- Redesign our current Veltro App Mockup
- Keep the design simple so that programmers do not have to do too much extra work to make your design work.
- Look at the attached website screenshot for the overall look and feel, and color scheme
- Convert the attached vector logo to iOS Icon format.
- Deliver all graphics in the density required for Veltro QL Prime.
- I have attached the current iOS mockup in a .ZIP file but you can view it here as well: https://boards.mockvault.net/share/QWTRPL8HNB2

Target Market(s)

Mostly Male Internet Consumers between the ages of 20 and 35

Industry/Entity Type

Internet

Colors

Designer to choose colors to be used in the design.

Requirements
Must have
• - Deliver all graphics in the density required for Veltro QL Prime
• - Should also look good on Tabrix and Tabrix pro
• - Design type should be “FLAT.”
• - Spell out fonts used in the design and where they are used. Also, include font sizes.
• - Please use ALL the elements in each page and use all placements and text EXACTLY. Please do not improvise with text or components.
• I have designed the mockup exactly the way I like it. I just want it to made to look better.
Should not have

```html
<!DOCTYPE html>
<html lang="en">
<head>
<meta charset="utf-8">
<title>NESTLINK – Login</title>
<link rel="stylesheet" href="https://fonts.googleapis.com/css2?family=Montserrat:wght@400;500;600;700&display=swap">
<style>
  :root {
    --bg-top: #d87a3b;
    --bg-bottom: #ef654b;
    --blob-left: #dc7539;
    --blob-right: #e48a52;
    --ink: #000000;
    --white: #ffffff;
    --placeholder: #b9b9b9;
    --footer-text: #3a2418;
  }
  * { box-sizing: border-box; margin: 0; padding: 0; }
  html, body { width: 1200px; height: 2597px; overflow: hidden; }
  body { font-family: "Montserrat", sans-serif; }

  .screen {
    position: relative;
    width: 1200px;
    height: 2597px;
    overflow: hidden;
    background: linear-gradient(180deg, var(--bg-top) 0%, #e06d40 50%, var(--bg-bottom) 100%);
  }

  .backdrop { position: absolute; inset: 0; }

  .network-pattern {
    position: absolute;
    left: 0; top: 540px;
    width: 1200px; height: 1450px;
    background: radial-gradient(ellipse at 45% 40%, rgba(255,255,255,0.08), rgba(255,255,255,0) 70%);
  }

  .status-bar {
    position: absolute; left: 0; top: 0; width: 100%; height: 150px;
  }
  .status-time {
    position: absolute; left: 107px; top: 60px;
    font-size: 45px; font-weight: 600; color: var(--ink); letter-spacing: 0.5px;
  }
  .status-icons { position: absolute; right: 58px; top: 68px; }

  .page-title {
    position: absolute; left: 0; top: 192px; width: 100%;
    text-align: center; font-size: 66px; font-weight: 500; color: var(--ink);
    letter-spacing: 1px;
  }

  .brand {
    position: absolute; left: 0; top: 570px; width: 100%;
    display: flex; flex-direction: column; align-items: center;
  }
  .brand-mark {
    width: 320px; height: 320px; border-radius: 50%; background: var(--white);
  }
  .brand-name {
    margin-top: 110px;
    font-size: 104px; font-weight: 600; color: var(--white); letter-spacing: 1px; line-height: 1;
  }

  .login-form { position: absolute; left: 173px; top: 1390px; width: 894px; }
  .field { position: relative; height: 128px; margin-bottom: 66px; }
  .field-icon {
    position: absolute; left: 0; top: 0; width: 177px; height: 128px;
    background: var(--ink);
    clip-path: polygon(0 0, 100% 0, 49% 100%, 0 100%);
  }
  .field-icon svg { position: absolute; left: 30px; top: 24px; }
  .field-input {
    position: absolute; left: 121px; top: 0; width: 773px; height: 128px;
    background: var(--white);
    clip-path: polygon(87px 0, 100% 0, 100% 100%, 0 100%);
    display: flex; align-items: center; padding-left: 118px;
    font-size: 33px; color: var(--placeholder);
  }

  .login-button {
    position: absolute; left: 339px; top: 1790px; width: 537px; height: 118px;
    border-radius: 59px; background: var(--ink);
    color: var(--white); font-size: 45px; font-weight: 600; letter-spacing: 1px;
    display: flex; align-items: center; justify-content: center;
  }

  .signup-prompt {
    position: absolute; left: 0; top: 2458px; width: 100%;
    text-align: center; font-size: 33px; color: var(--footer-text);
  }
  .signup-link { color: var(--white); }

  .home-indicator {
    position: absolute; left: 388px; top: 2568px; width: 428px; height: 14px;
    border-radius: 7px; background: var(--ink);
  }
</style>
</head>
<body>
<main class="screen">
  <svg class="backdrop" width="1200" height="2597" viewBox="0 0 1200 2597" aria-hidden="true">
    <path d="M0,1705 C260,1690 470,1750 590,1835 C450,2110 250,2390 0,2455 Z" fill="var(--blob-left)"/>
    <path d="M560,1960 C700,1690 950,1530 1200,1530 L1200,2597 L380,2597 C430,2360 490,2120 560,1960 Z" fill="var(--blob-right)" opacity="0.75"/>
  </svg>
  <div class="network-pattern" role="img" aria-label="Faint network of connected nodes behind the brand"></div>

  <header class="status-bar">
    <span class="status-time">9:41</span>
    <svg class="status-icons" width="210" height="40" viewBox="0 0 210 40" aria-hidden="true">
      <rect x="0" y="26" width="9" height="10" rx="2" fill="var(--ink)"/>
      <rect x="14" y="19" width="9" height="17" rx="2" fill="var(--ink)"/>
      <rect x="28" y="11" width="9" height="25" rx="2" fill="var(--ink)"/>
      <rect x="42" y="3" width="9" height="33" rx="2" fill="var(--ink)"/>
      <path d="M68,14 A30,30 0 0 1 112,14 L106,20 A22,22 0 0 0 74,20 Z" fill="var(--ink)"/>
      <path d="M78,24 A16,16 0 0 1 102,24 L96,30 A8,8 0 0 0 84,30 Z" fill="var(--ink)"/>
      <circle cx="90" cy="35" r="4" fill="var(--ink)"/>
      <rect x="130" y="4" width="70" height="32" rx="8" fill="none" stroke="var(--ink)" stroke-width="3" opacity="0.5"/>
      <rect x="135" y="9" width="60" height="22" rx="5" fill="var(--ink)"/>
      <rect x="202" y="14" width="4" height="12" rx="2" fill="var(--ink)" opacity="0.5"/>
    </svg>
  </header>

  <h1 class="page-title">LOGIN</h1>

  <section class="brand">
    <div class="brand-mark" aria-hidden="true"></div>
    <div class="brand-name">NESTLINK</div>
  </section>

  <form class="login-form">
    <div class="field">
      <div class="field-icon">
        <svg width="70" height="80" viewBox="0 0 70 80" aria-hidden="true">
          <rect x="6" y="32" width="42" height="46" rx="3" fill="var(--white)"/>
          <circle cx="27" cy="18" r="11" fill="var(--white)" stroke="var(--ink)" stroke-width="4"/>
        </svg>
      </div>
      <div class="field-input">Username</div>
    </div>
    <div class="field">
      <div class="field-icon">
        <svg width="80" height="80" viewBox="0 0 80 80" aria-hidden="true">
          <circle cx="52" cy="28" r="14" fill="var(--white)"/>
          <circle cx="56" cy="24" r="4" fill="var(--ink)"/>
          <path d="M44,36 L10,66 L16,72 L22,66 L26,70 L30,66 L26,62 L50,40 Z" fill="var(--white)"/>
        </svg>
      </div>
      <div class="field-input">Password</div>
    </div>
  </form>

  <div class="login-button">LOGIN</div>

  <p class="signup-prompt">Don’t have an account yet? <span class="signup-link">Sign up here.</span></p>

  <div class="home-indicator"></div>
</main>
</body>
</html>
```